Telmoro Business Card

I already have the conplay logo. I need to develop a professional business card layout

Target Market(s)

Business

Industry/Entity Type

Business

Contact Information for Business Card

Company Name: Telmoro Limited

Font styles to use
Sans Serif

Colors

Designer to choose colors to be used in the design.

Requirements
Must have
• Use current logo
• Need two card size options:
• Small Card: 70mm x 28mm (Landscape)
• Square Card: 65mm x 65mm
Nice to have
• I will need 8-10 files for each name, number and email address (details to follow)

```html
<!DOCTYPE html>
<html lang="en">
<head>
<meta charset="utf-8">
<title>Telmoro Limited – Business Card</title>
<link rel="stylesheet" href="https://fonts.googleapis.com/css2?family=Oswald:wght@300;400;500&family=Roboto:wght@300;400&display=swap">
<style>
  :root {
    --ink-blue: #1c3a9e;
    --icon-blue: #1a3aa0;
    --white: #ffffff;
    --pink: #f27bd8;
    --violet: #c98cf2;
    --sky: #a9c4ff;
    --lemon: #f6f9a8;
    --blush: #f7c6e4;
    --paper: #fbf8fb;
    --shadow: rgba(20, 10, 40, 0.75);
  }
  * { margin: 0; padding: 0; box-sizing: border-box; }
  html, body { width: 1200px; height: 480px; overflow: hidden; background: var(--white); }
  .card {
    position: relative;
    width: 1200px;
    height: 480px;
    overflow: hidden;
    background:
      radial-gradient(ellipse 380px 260px at 960px 350px, var(--lemon) 0%, rgba(246,249,168,0) 100%),
      radial-gradient(ellipse 520px 240px at 760px 0px, var(--sky) 0%, rgba(169,196,255,0) 100%),
      radial-gradient(ellipse 520px 420px at 60px 60px, var(--pink) 0%, rgba(242,123,216,0) 100%),
      radial-gradient(ellipse 560px 420px at 380px 300px, var(--blush) 0%, rgba(247,198,228,0) 100%),
      linear-gradient(90deg, var(--violet) 0%, var(--blush) 40%, var(--paper) 70%, var(--white) 100%);
    font-family: 'Oswald', sans-serif;
  }
  .streaks { position: absolute; inset: 0; width: 1200px; height: 480px; }

  .identity {
    position: absolute;
    left: 200px;
    top: 160px;
    width: 380px;
    text-align: center;
  }
  .brand-name {
    font-family: 'Oswald', sans-serif;
    font-weight: 500;
    font-size: 60px;
    line-height: 60px;
    letter-spacing: 0.02em;
    color: var(--icon-blue);
  }
  .brand-legal {
    font-family: 'Roboto', sans-serif;
    font-weight: 300;
    font-size: 23px;
    color: var(--white);
    text-align: right;
    padding-right: 58px;
    margin-top: 2px;
  }
  .identity-rule {
    position: absolute;
    left: 200px;
    top: 266px;
    width: 380px;
    height: 10px;
    background: radial-gradient(ellipse at center, var(--shadow) 0%, rgba(20,10,40,0) 70%);
  }
  .person { position: absolute; left: 200px; top: 296px; width: 380px; text-align: center; }
  .person-name {
    font-family: 'Oswald', sans-serif;
    font-weight: 400;
    font-size: 44px;
    letter-spacing: 0.16em;
    color: var(--ink-blue);
    line-height: 56px;
  }
  .person-role {
    font-family: 'Roboto', sans-serif;
    font-weight: 300;
    font-size: 26px;
    color: var(--ink-blue);
    text-align: right;
    padding-right: 58px;
    line-height: 30px;
  }

  .divider {
    position: absolute;
    left: 622px;
    top: 80px;
    width: 10px;
    height: 340px;
    background: radial-gradient(ellipse at center, var(--shadow) 0%, rgba(20,10,40,0) 70%);
  }

  .contacts { position: absolute; left: 686px; top: 0; width: 480px; height: 480px; }
  .contact-row { position: absolute; left: 0; display: flex; align-items: flex-start; }
  .contact-icon {
    width: 40px; height: 40px;
    border-radius: 6px;
    background: var(--icon-blue);
    display: flex; align-items: center; justify-content: center;
    flex-shrink: 0;
  }
  .contact-text {
    margin-left: 24px;
    margin-top: 0;
    font-family: 'Oswald', sans-serif;
    font-weight: 400;
    font-size: 17px;
    line-height: 23px;
    color: var(--ink-blue);
    text-transform: uppercase;
  }
  .row-location { top: 140px; }
  .row-phone { top: 226px; }
  .row-web { top: 318px; }
</style>
</head>
<body>
<main class="card">
  <svg class="streaks" viewBox="0 0 1200 480" aria-hidden="true">
    <polygon points="0,330 260,480 180,480 0,380" fill="#ffffff" opacity="0.35"/>
    <polygon points="120,0 420,210 420,240 60,0" fill="#ffffff" opacity="0.18"/>
    <polygon points="0,200 140,480 100,480 0,270" fill="#ffffff" opacity="0.22"/>
  </svg>

  <section class="identity">
    <div class="brand-name">TELMORO</div>
    <div class="brand-legal">Telmoro Limited</div>
  </section>
  <div class="identity-rule"></div>

  <section class="person">
    <div class="person-name">EVAN HALE</div>
    <div class="person-role">Creative Director</div>
  </section>

  <div class="divider"></div>

  <section class="contacts">
    <div class="contact-row row-location">
      <div class="contact-icon">
        <svg width="22" height="26" viewBox="0 0 22 26" aria-hidden="true">
          <path d="M11 1C5.8 1 2 4.9 2 9.8 2 16 11 25 11 25s9-9 9-15.2C20 4.9 16.2 1 11 1z" fill="none" stroke="#fff" stroke-width="2"/>
          <circle cx="11" cy="10" r="3.2" fill="#fff"/>
        </svg>
      </div>
      <div class="contact-text">Your City Location<br>Street Address, Zipcode, NY City, USA</div>
    </div>

    <div class="contact-row row-phone">
      <div class="contact-icon">
        <svg width="22" height="24" viewBox="0 0 22 24" aria-hidden="true">
          <path d="M6 1.5c1 0 2.2 3.6 2.2 4.6 0 1-2 1.6-2 2.8 0 1.8 3.5 7.4 5.4 8 1 .3 2-1.5 3-1.3 1 .2 3.6 3 3.4 4-.3 1.4-2.6 3-4.2 2.9C8 22 1.5 13 2 6.5 2.1 4.3 4.5 1.5 6 1.5z" fill="none" stroke="#fff" stroke-width="1.8"/>
        </svg>
      </div>
      <div class="contact-text">+00 1111 2222 6666<br>+00 1111 4444 9999</div>
    </div>

    <div class="contact-row row-web">
      <div class="contact-icon">
        <svg width="26" height="26" viewBox="0 0 26 26" aria-hidden="true">
          <g fill="none" stroke="#fff" stroke-width="1.6">
            <circle cx="13" cy="13" r="11"/>
            <ellipse cx="13" cy="13" rx="5" ry="11"/>
            <line x1="2" y1="13" x2="24" y2="13"/>
            <line x1="4" y1="7.5" x2="22" y2="7.5"/>
            <line x1="4" y1="18.5" x2="22" y2="18.5"/>
          </g>
        </svg>
      </div>
      <div class="contact-text">www.yourcompany.com<br>mail@yourcompany.com</div>
    </div>
  </section>
</main>
</body>
</html>
```